Business Card Design with new logo

Dorian Pelleway 4172
E 118th St Alder Falls, IL 62999
Cell: 217-555-0193
pellewayrestoration@mailvane.test

Classic Car Restoration Services Buy Sell Trade Consign

Dorian Pelleway 9698
Cell: 217-555-0193

```html
<!DOCTYPE html>
<html lang="en">
<head>
<meta charset="utf-8">
<title>Pelleway Restoration LLC – Business Cards</title>
<link href="https://fonts.googleapis.com/css2?family=Lato:wght@400;700&family=Roboto:wght@700;900&display=swap" rel="stylesheet">
<style>
  :root {
    --navy: #13242f;
    --paper: #ffffff;
    --stone: #e6e6e6;
    --stone-line: #f7f7f7;
    --orange: #ee5222;
    --red: #c8282a;
    --ink: #2b2b2b;
    --backdrop: #2a2a2a;
  }
  * { margin: 0; padding: 0; box-sizing: border-box; }
  html, body { width: 1200px; height: 1200px; overflow: hidden; }
  body { background: var(--backdrop); position: relative; }

  .card {
    position: absolute;
    left: 160px;
    width: 880px;
    height: 500px;
    background: var(--navy);
    padding: 26px;
  }
  .card--front { top: 60px; }
  .card--back { top: 630px; }

  /* Front */
  .front-face {
    width: 100%; height: 100%;
    background: var(--paper);
    padding: 12px;
  }
  .front-frame {
    width: 100%; height: 100%;
    border: 2px solid var(--navy);
    position: relative;
    display: flex; flex-direction: column; align-items: center; justify-content: center;
  }
  .brand {
    display: flex; align-items: center; gap: 18px;
    margin-top: -40px;
  }
  .brand__mark { width: 46px; height: 46px; background: var(--red); flex: none; }
  .brand__name {
    font-family: "Roboto", sans-serif; font-weight: 900;
    color: var(--navy); font-size: 50px; letter-spacing: 2px;
    text-transform: uppercase; line-height: 1.1;
  }
  .brand__sub {
    display: block; font-size: 26px; letter-spacing: 14px;
  }
  .tagline {
    position: absolute; bottom: 26px; left: 0; right: 0;
    display: flex; align-items: center; justify-content: center; gap: 14px;
    font-family: "Roboto", sans-serif; font-weight: 700;
    font-size: 21px; color: var(--navy);
  }
  .car-icon { width: 44px; height: 34px; fill: var(--navy); }

  /* Back */
  .back-face {
    width: 100%; height: 100%;
    background: var(--stone);
    padding: 14px;
    display: flex; gap: 10px;
  }
  .contact-list {
    width: 530px; flex: none;
    display: flex; flex-direction: column; gap: 8px;
  }
  .contact-row {
    flex: 1;
    border: 3px solid var(--stone-line);
    display: flex; align-items: center; gap: 30px;
    padding-left: 24px;
    font-family: "Lato", sans-serif; font-size: 21px; color: var(--ink);
    line-height: 1.4;
    white-space: nowrap;
  }
  .contact-row__icon {
    width: 92px; height: 88px; flex: none;
    background: var(--orange);
    display: flex; align-items: center; justify-content: center;
  }
  .contact-row__icon svg { width: 48px; height: 48px; fill: none; stroke: #fff; stroke-width: 3; }
  .brand-panel {
    flex: 1;
    border: 3px solid var(--stone-line);
    display: flex; align-items: center; justify-content: center;
  }
  .brand-panel .brand { margin-top: 0; gap: 10px; }
  .brand-panel .brand__mark { width: 24px; height: 24px; }
  .brand-panel .brand__name { font-size: 28px; letter-spacing: 1px; }
  .brand-panel .brand__sub { font-size: 13px; letter-spacing: 4px; }
</style>
</head>
<body>

<section class="card card--front">
  <div class="front-face">
    <div class="front-frame">
      <div class="brand">
        <span class="brand__mark"></span>
        <span class="brand__name">Pelleway<span class="brand__sub">Restoration LLC</span></span>
      </div>
      <p class="tagline">
        <svg class="car-icon" viewBox="0 0 44 34" aria-hidden="true"><path d="M8 14 L12 4 Q13 2 16 2 H28 Q31 2 32 4 L36 14 Q42 15 42 20 V28 H37 V32 H31 V28 H13 V32 H7 V28 H2 V20 Q2 15 8 14 Z M12 13 H32 L29 5 H15 Z"/><circle cx="10" cy="21" r="3" fill="#fff"/><circle cx="34" cy="21" r="3" fill="#fff"/></svg>
        Classic Car Restoration Services Buy Sell Trade Consign
        <svg class="car-icon" viewBox="0 0 44 34" aria-hidden="true"><path d="M8 14 L12 4 Q13 2 16 2 H28 Q31 2 32 4 L36 14 Q42 15 42 20 V28 H37 V32 H31 V28 H13 V32 H7 V28 H2 V20 Q2 15 8 14 Z M12 13 H32 L29 5 H15 Z"/><circle cx="10" cy="21" r="3" fill="#fff"/><circle cx="34" cy="21" r="3" fill="#fff"/></svg>
      </p>
    </div>
  </div>
</section>

<section class="card card--back">
  <div class="back-face">
    <div class="contact-list">
      <div class="contact-row">
        <span class="contact-row__icon">
          <svg viewBox="0 0 48 48" aria-hidden="true"><path d="M6 24 L24 8 L42 24"/><path d="M12 20 V40 H36 V20"/><path d="M20 40 V28 H28 V40"/></svg>
        </span>
        <span>Dorian Pelleway 4172<br>E 118th St Alder Falls, IL 62999</span>
      </div>
      <div class="contact-row">
        <span class="contact-row__icon">
          <svg viewBox="0 0 48 48" aria-hidden="true"><path d="M14 8 L20 16 L16 21 Q20 29 27 32 L32 28 L40 34 L36 40 Q22 40 12 28 Q7 20 8 12 Z" fill="#fff" stroke="none"/></svg>
        </span>
        <span>217-555-0193</span>
      </div>
      <div class="contact-row">
        <span class="contact-row__icon">
          <svg viewBox="0 0 48 48" aria-hidden="true"><rect x="6" y="12" width="36" height="24"/><path d="M6 12 L24 27 L42 12"/><path d="M6 36 L19 23 M42 36 L29 23"/></svg>
        </span>
        <span>pellewayrestoration@mailvane.test</span>
      </div>
    </div>
    <div class="brand-panel">
      <div class="brand">
        <span class="brand__mark"></span>
        <span class="brand__name">Pelleway<span class="brand__sub">Restoration LLC</span></span>
      </div>
    </div>
  </div>
</section>

</body>
</html>
```